I want to revise my business card design and get a more modern and up to date design.

Brolvane Handyman Sevices originated from a family-owned and operated contractor business, performing home renovation, addition, and construction work in the NYC area since 2004. Today, we specialize in reliable and affordable handyman services for residential and commercial clients In 2014, we expanded to northern New Jersey. In 2016, we brought quality home improvement and repair services to new Bucks County, PA, and nearby New Jersey areas.
Target Market(s)
Home owners and business that might be looking for a General contractor, handyman, cleaning services and Home maintenance and property.
Industry/Entity Type
Construction Company
Contact Information for Business Card
I am open to new ideas
Colors
Designer to choose colors to be used in the design.
Look and feel
Each slider illustrates characteristics of the customer's brand and the style your logo design should communicate.

```html
<!DOCTYPE html>
<html lang="en">
<head>
<meta charset="utf-8">
<title>Brolvane Handyman Sevices – Business Card</title>
<link rel="stylesheet" href="https://fonts.googleapis.com/css2?family=Poppins:wght@300;400;600;800&display=swap">
<style>
  :root{
    --brand-red:#d2161e;
    --ink:#151515;
    --muted:#4a4a4a;
    --card:#f7f6f3;
    --backdrop:#e9e7e3;
    --rule:#9a9a9a;
  }
  *{box-sizing:border-box;margin:0;padding:0}
  html,body{width:1200px;height:1050px;overflow:hidden}
  body{
    background:var(--backdrop);
    font-family:"Poppins",sans-serif;
    color:var(--ink);
    position:relative;
  }
  .card{
    position:absolute;left:220px;width:760px;height:434px;
    background:var(--card);
    border-bottom:6px solid var(--brand-red);
    box-shadow:0 14px 30px rgba(0,0,0,.16);
    overflow:hidden;
  }
  .card--front{top:60px}
  .card--back{top:556px}

  /* front */
  .brand{position:absolute;left:70px;top:150px;display:flex;align-items:center;gap:16px}
  .brand__dot{width:62px;height:62px;border-radius:50%;background:var(--brand-red);flex:none}
  .brand__name{font-weight:800;font-size:50px;line-height:1;letter-spacing:-1px;color:var(--ink)}
  .brand__tag{position:absolute;left:148px;top:212px;font-size:12px;font-weight:400;letter-spacing:4px;color:var(--muted)}
  .divider{position:absolute;left:405px;top:135px;width:1.5px;height:150px;background:var(--rule)}
  .contact{position:absolute;left:430px;top:132px}
  .contact__name{font-weight:800;font-size:22px;color:var(--brand-red);letter-spacing:.5px;text-transform:uppercase}
  .contact__title{font-size:15px;font-weight:400;color:var(--muted);margin-bottom:12px}
  .contact__row{display:flex;align-items:center;gap:10px;font-size:15px;font-weight:400;color:var(--ink);line-height:26px}
  .contact__row svg{width:14px;height:14px;flex:none}

  /* back */
  .back-mark{position:absolute;left:-70px;top:-60px;width:230px;height:230px;border-radius:50%;background:var(--brand-red)}
  .back-brand{position:absolute;left:230px;top:150px}
  .back-brand__name{font-weight:800;font-size:92px;line-height:1;letter-spacing:-2px}
  .back-brand__tag{font-size:17px;letter-spacing:7px;color:var(--muted);margin-top:4px}
  .back-services{position:absolute;right:56px;bottom:52px;text-align:left}
  .back-services__lead{font-size:16px;font-weight:400}
  .back-services__list{font-size:16px;font-weight:400;display:flex;align-items:center;gap:8px;margin-top:2px}
  .bullet{width:8px;height:8px;background:var(--brand-red);display:inline-block}
</style>
</head>
<body>

<section class="card card--front" aria-label="Business card front">
  <div class="brand">
    <span class="brand__dot"></span>
    <span class="brand__name">Brolvane</span>
  </div>
  <div class="brand__tag">HANDYMAN SERVICES</div>

  <div class="divider"></div>

  <div class="contact">
    <div class="contact__name">Marco Delgado</div>
    <div class="contact__title">Senior Consultant</div>
    <div class="contact__row">
      <svg viewBox="0 0 24 24" fill="var(--brand-red)"><path d="M6.6 10.8a15.1 15.1 0 0 0 6.6 6.6l2.2-2.2a1 1 0 0 1 1-.25 11.4 11.4 0 0 0 3.6.57 1 1 0 0 1 1 1V20a1 1 0 0 1-1 1A17 17 0 0 1 3 4a1 1 0 0 1 1-1h3.5a1 1 0 0 1 1 1c0 1.25.2 2.45.57 3.57a1 1 0 0 1-.25 1z"/></svg>
      <span>(402) 555-0187</span>
    </div>
    <div class="contact__row">
      <svg viewBox="0 0 24 24" fill="none" stroke="var(--brand-red)" stroke-width="2.4"><rect x="2" y="5" width="20" height="14" rx="1"/><path d="M2 6l10 7 10-7"/></svg>
      <span>brolvanehandyman@mail.com</span>
    </div>
    <div class="contact__row">
      <svg viewBox="0 0 24 24" fill="none" stroke="var(--brand-red)" stroke-width="2.2"><circle cx="12" cy="12" r="10"/><path d="M2 12h20M12 2c3 3 3 17 0 20M12 2c-3 3-3 17 0 20"/></svg>
      <span>www.brolvanehandyman.com</span>
    </div>
  </div>
</section>

<section class="card card--back" aria-label="Business card back">
  <div class="back-mark"></div>
  <div class="back-brand">
    <div class="back-brand__name">Brolvane</div>
    <div class="back-brand__tag">HANDYMAN SERVICES</div>
  </div>
  <div class="back-services">
    <div class="back-services__lead">Residential &amp; Commercial Contractor</div>
    <div class="back-services__list">
      <span>Repair</span><span class="bullet"></span>
      <span>Improve</span><span class="bullet"></span>
      <span>Maintain</span><span class="bullet"></span>
      <span>Remodel</span>
    </div>
  </div>
</section>

</body>
</html>
```